Deliver a professional and engaging investment propsal.

I am appealing to highend smart investors and need a high quality, engaging and formal presentation in PDF.
DropBox: https://www.filemarsh.net/sh/q8wz3kdmv2tanp7/BCxRp4LfWmZq9TnYeJ2sKo7vH?dl=0
Text for project is in Dropbox called New Proposal Final
Along with past much older attempts of this job.
Any additional ideas to enable a better outcome would be appreicated.

```html
<!DOCTYPE html>
<html lang="en">
<head>
<meta charset="utf-8">
<title>Joint Venture Proposal – Ridgeline Town Center</title>
<link rel="stylesheet" href="https://fonts.googleapis.com/css2?family=Lato:ital,wght@0,300;0,400;0,700;0,900;1,400;1,700&family=Fira+Sans:ital,wght@1,400;1,500&display=swap">
<style>
  :root{
    --blue:#1273bd;
    --blue-light:#3d9ad9;
    --ink:#4a4a4a;
    --ink-dark:#333;
    --paper:#ffffff;
  }
  *{box-sizing:border-box;margin:0;padding:0}
  html,body{width:867px;height:1200px;overflow:hidden;background:var(--paper)}
  body{position:relative;font-family:"Lato",sans-serif;color:var(--ink)}
  .abs{position:absolute}

  .title-light{left:92px;top:126px;font-size:32px;font-weight:300;color:var(--ink);line-height:1}
  .title-bold{left:91px;top:160px;font-size:39px;font-weight:900;color:var(--blue);line-height:1;letter-spacing:.3px}
  .title-rule{left:92px;top:213px;width:676px;height:4px;background:var(--blue)}
  .intro{left:92px;top:235px;width:680px;font-size:15px;line-height:19px;color:var(--ink)}

  .section-head{left:92px;top:360px;font-family:"Fira Sans",sans-serif;font-style:italic;font-weight:400;font-size:22px;color:var(--blue)}
  .divider{left:353px;top:369px;width:1px;height:731px;background:var(--ink-dark)}

  .options{left:97px;top:402px;width:242px;list-style:none}
  .options li{position:relative;padding-left:23px;font-size:12.2px;line-height:15.6px;color:var(--ink);margin-bottom:15.5px}
  .options li::before{content:"";position:absolute;left:0;top:3px;width:7px;height:7px;background:var(--blue);border-radius:1px}
  .hl{color:var(--blue);font-weight:700;font-style:italic}

  .pull-quote{left:384px;top:386px;width:430px;font-family:"Fira Sans",sans-serif;font-style:italic;font-size:20px;line-height:24px;color:var(--blue)}
  .body-copy{left:384px;top:530px;width:420px;font-size:15px;line-height:19px;color:var(--ink)}
  .note{left:384px;top:603px;width:425px;list-style:none}
  .note li{position:relative;padding-left:22px;font-size:12.4px;line-height:15.5px}
  .note li::before{content:"";position:absolute;left:4px;top:4px;width:6px;height:6px;background:var(--ink)}

  .plan-card{left:376px;top:732px;width:430px;height:368px;background:#fff;box-shadow:0 1px 4px rgba(0,0,0,.3)}
  .plan-kicker{position:absolute;left:0;width:100%;top:6px;text-align:center;font-size:6.5px;letter-spacing:.2px;color:#444}
  .plan-name{position:absolute;left:0;width:100%;top:16px;text-align:center;font-size:11px;font-weight:900;font-style:italic;color:#111}
  .site-plan{position:absolute;left:30px;top:29px;width:370px;height:223px;background:linear-gradient(135deg,#7f9a5a,#a9b98d 45%,#8aa26a)}
  .photo{position:absolute;top:257px;height:64px}
  .photo-1{left:19px;width:126px;background:linear-gradient(#b9c9dc,#c9b79f)}
  .photo-2{left:150px;width:143px;background:linear-gradient(#a9c3e0,#6d8a4f 60%,#9a5a3a)}
  .photo-3{left:299px;width:109px;background:linear-gradient(#8fb0d8,#b0684a 50%,#6b4e3a)}
  .plan-band{position:absolute;left:0;bottom:0;width:100%;height:31px;background:var(--blue)}

  .footer-name{right:420px;top:1149px;font-size:16px;color:var(--ink-dark);letter-spacing:.1px;white-space:nowrap}
  .footer-bar-a{left:457px;top:1151px;width:132px;height:13px;background:var(--blue-light)}
  .footer-bar-b{left:589px;top:1151px;width:278px;height:13px;background:var(--blue)}
  .footer-line-l{left:0;top:1172px;width:57px;height:2px;background:var(--blue)}
  .footer-line-r{left:91px;top:1172px;width:776px;height:1px;background:var(--blue)}
  .page-num{left:66px;top:1163px;font-size:16px;color:var(--ink-dark)}
</style>
</head>
<body>
  <div class="abs title-light">Joint Venture</div>
  <h1 class="abs title-bold">PROPOSAL</h1>
  <div class="abs title-rule"></div>

  <p class="abs intro">We have an incredible property, Ridgeline Business Park, located at 1780 Prairie Route 12 Brennan County, Harlow City, North Dakota 58990 USA which we have fully funded with cashand now need a joint venture partner, buyer or lender to get this project to completion and producing a substantial profit we all can share.</p>

  <h2 class="abs section-head">Participation Options</h2>
  <div class="abs divider"></div>

  <ul class="abs options">
    <li>A joint venture partnerwould support all the costs developing the property without the <span class="hl">upfront costs</span> of the property purchase.</li>
    <li>All sales would be split to ensure both parties are paid out in such a way that both are paid out in full at the same time then a <span class="hl">50/50 profit</span> share split on all remaining sales.</li>
    <li>Contract drawn up <span class="hl">protecting</span> and <span class="hl">supporting</span> both parties on agreed terms.</li>
    <li>As a potential joint venture partner, I would cover the full property (57.7 acres) cost as mentioned of <span class="hl">$124,784</span> per acre (57.7 acres). <span class="hl">($7,200,000)</span></li>
    <li>Point venture partner to supply the development costs estimated to be around <span class="hl">$65,000</span> an acre estimated pending tender selection and additional refundable security bonds held with the Harlow City on development works.</li>
    <li>Development costs could be in up to three stages to <span class="hl">lower outlay</span> and <span class="hl">limit exposure</span> if so desired, however it will take longer to complete and bring to market.</li>
    <li>A buyercan be fully supported by myself to oversee the full project and outcomes and support the budgets of construction and sales to get the <span class="hl">highest returns</span> for a small fee.</li>
    <li>Financingon excellent terms allowing <span class="hl">12 to 18 months</span> for income streams and could be linked to a joint venture option / profit share.</li>
  </ul>

  <p class="abs pull-quote">Our property is located on the best oil reserves in the world in North Dakota USA, with more oil than any other county in the Bakken Basin and with the lowest recoverable costs of $24 a barrel.</p>

  <p class="abs body-copy">We own the property and need a partner to develop the site and bring to the market at half the cost of competing business parks in the area.</p>

  <ul class="abs note">
    <li>To purchase the property, you would need to contact me directly and I can introduce you to our realtor who will discount his commission from 6% to 5% which is a significant saving.</li>
  </ul>

  <figure class="abs plan-card">
    <div class="plan-kicker">60 ACRE MIXED-USE DEVELOPMENT</div>
    <div class="plan-name">RIDGELINE TOWN CENTER</div>
    <div class="site-plan" role="img" aria-label="Aerial site plan of the 60 acre mixed-use development showing lots, roads and landscaping, with one lot marked sold"></div>
    <div class="photo photo-1" role="img" aria-label="Rendering of a hotel building marked coming soon"></div>
    <div class="photo photo-2" role="img" aria-label="Rendering of a brick retail building with landscaped plaza"></div>
    <div class="photo photo-3" role="img" aria-label="Rendering of a two-storey brick main street storefront"></div>
    <div class="plan-band"></div>
  </figure>

  <div class="abs footer-name">RIDGELINE TOWN CENTER</div>
  <div class="abs footer-bar-a"></div>
  <div class="abs footer-bar-b"></div>
  <div class="abs footer-line-l"></div>
  <div class="abs page-num">2</div>
  <div class="abs footer-line-r"></div>
</body>
</html>
```